Larkmoor Health- Core Values Graphic for Visual Appeal

I would like a poster that could take these written core values from our organization and create a graphic that we could use for our staff and employees. I would also like to incorporate our branding into this project. Thank you!

Target Market(s)

To helps patients and employees understand the core values of our organization

Industry/Entity Type

Healthcare

Requirements
Must have
• Match our branding
Nice to have
• Please use your creativity!
Should not have
• Overly complex/ busy

```html
<!DOCTYPE html>
<html lang="en">
<head>
<meta charset="utf-8">
<title>Larkmoor Health – Core Values</title>
<link rel="stylesheet" href="https://fonts.googleapis.com/css2?family=Poppins:wght@400;600;700;800&display=swap">
<style>
  :root {
    --blue: #29a8e0;
    --navy: #0d3f63;
    --charcoal: #3d3d3f;
    --ink: #2b2b2b;
    --line: #333333;
    --paper: #ffffff;
    --backdrop: #f1f1f1;
    --band: #222222;
  }
  * { box-sizing: border-box; margin: 0; padding: 0; }
  html, body { width: 1200px; height: 2322px; overflow: hidden; }
  body {
    background: var(--backdrop);
    font-family: "Poppins", sans-serif;
    color: var(--ink);
    position: relative;
  }
  .poster {
    position: absolute;
    left: 50px; top: 427px;
    width: 1100px; height: 1468px;
    background: var(--paper);
    box-shadow: 0 6px 24px rgba(0,0,0,0.18);
    overflow: hidden;
  }
  .brand {
    position: absolute;
    left: 60px; top: 110px;
    width: 290px;
    display: flex; flex-direction: column; align-items: center; gap: 18px;
  }
  .brand-dot {
    width: 84px; height: 84px; border-radius: 50%;
    background: var(--blue);
  }
  .brand-name {
    font-weight: 700; font-size: 34px; line-height: 1.1;
    color: var(--charcoal); text-align: center;
  }
  .headline {
    position: absolute; left: 372px; top: 40px;
    font-weight: 800; line-height: 0.86; letter-spacing: -2px;
  }
  .headline .core { display: block; font-size: 162px; color: var(--blue); }
  .headline .values { display: block; font-size: 162px; color: var(--charcoal); }
  .intro {
    position: absolute; left: 62px; top: 360px; width: 990px;
    font-size: 27.5px; line-height: 32px; color: var(--ink);
  }
  .card, .tile {
    position: absolute;
    border: 2.5px solid var(--line);
    border-radius: 6px;
    background: var(--paper);
  }
  .tile { width: 212px; height: 182px; padding: 8px; }
  .tile-fill { width: 100%; height: 100%; border-radius: 3px; }
  .tile-fill.blue { background: var(--blue); }
  .tile-fill.navy { background: var(--navy); }
  .card { height: 182px; padding: 16px 28px 0 28px; }
  .card-title {
    font-weight: 800; font-size: 42px; line-height: 1.1; letter-spacing: 0.5px;
  }
  .card-title.blue { color: var(--blue); }
  .card-title.navy { color: var(--navy); }
  .card-text { font-size: 16.5px; line-height: 18.6px; color: var(--ink); margin-top: 2px; }
  .links { position: absolute; left: 0; top: 0; }
  .footer {
    position: absolute; left: 0; bottom: 0; width: 100%; height: 90px;
    background: var(--band);
    display: flex; align-items: center; justify-content: center;
    font-weight: 600; font-size: 27px; letter-spacing: 7px; color: #fff;
  }
  .footer .accent { color: var(--blue); }
</style>
</head>
<body>
  <main class="poster">
    <div class="brand">
      <span class="brand-dot"></span>
      <span class="brand-name">Larkmoor Health</span>
    </div>

    <h1 class="headline"><span class="core">CORE</span><span class="values">VALUES</span></h1>

    <p class="intro">These core values are the spirit of who we are as a healthcare team. They guide our actions, unite us in purpose, and ensure that we provide world-class care while fostering a positive and supportive atmosphere within our team:</p>

    <svg class="links" width="1100" height="1468" viewBox="0 0 1100 1468" aria-hidden="true">
      <g stroke="#555" stroke-width="1.5" fill="none">
        <line x1="276" y1="615" x2="347" y2="615"/>
        <line x1="170" y1="706" x2="170" y2="735"/>
        <line x1="748" y1="826" x2="819" y2="826"/>
        <line x1="925" y1="917" x2="925" y2="948"/>
        <line x1="276" y1="1039" x2="347" y2="1039"/>
        <line x1="170" y1="1130" x2="170" y2="1165"/>
        <line x1="748" y1="1256" x2="819" y2="1256"/>
      </g>
      <g fill="#29a8e0">
        <circle cx="276" cy="615" r="4"/><circle cx="347" cy="615" r="4"/>
        <circle cx="170" cy="720" r="4"/>
        <circle cx="925" cy="932" r="4"/>
        <circle cx="276" cy="1039" r="4"/><circle cx="347" cy="1039" r="4"/>
      </g>
      <g fill="#0d3f63">
        <circle cx="748" cy="826" r="4"/><circle cx="819" cy="826" r="4"/>
        <circle cx="170" cy="1147" r="4"/>
        <circle cx="748" cy="1256" r="4"/><circle cx="819" cy="1256" r="4"/>
      </g>
    </svg>

    <div class="tile" style="left:64px; top:524px;">
      <div class="tile-fill blue" role="img" aria-label="Icon of a family with parents and children"></div>
    </div>
    <section class="card" style="left:347px; top:524px; width:684px;">
      <h2 class="card-title blue">FAMILY</h2>
      <p class="card-text">At the heart of our mission is the commitment to provide high-quality, affordable healthcare in a comforting and uplifting family-oriented environment. Just as our community is our extended family, every patient is a cherished member of our healthcare family. We treat each individual with the same care, compassion, and respect we would offer to our own loved ones.</p>
    </section>

    <section class="card" style="left:64px; top:735px; width:684px;">
      <h2 class="card-title navy">EXCELLENCE</h2>
      <p class="card-text">In line with our goal, we aspire not only to alleviate pain but also to inspire patients to become active participants in their well-being. We believe in empowering our patients through education and compassion. Our pursuit of excellence is unwavering, driven by our dedication to continuously improve our services at every level, ensuring that our community receives nothing less than exceptional care.</p>
    </section>
    <div class="tile" style="left:819px; top:735px;">
      <div class="tile-fill navy" role="img" aria-label="Icon of a hand holding an award ribbon with a tick"></div>
    </div>

    <div class="tile" style="left:64px; top:948px;">
      <div class="tile-fill blue" role="img" aria-label="Icon of interlocking puzzle pieces"></div>
    </div>
    <section class="card" style="left:347px; top:948px; width:684px;">
      <h2 class="card-title blue">INTEGRITY</h2>
      <p class="card-text">In our healthcare team, 'Integrity' is non-negotiable.&nbsp; Our purpose is deeply rooted in ethics, integrity, and professional standards. We operate with the utmost integrity in every aspect of our work, adhering to the highest ethical principles. We understand that trust is the foundation of healthcare, and we are committed to maintaining the trust our community places in us.</p>
    </section>

    <section class="card" style="left:64px; top:1165px; width:684px;">
      <h2 class="card-title navy">SERVICE</h2>
      <p class="card-text">Our vision is grounded in the belief that every person possesses the innate potential for true health. We aim to facilitate the body's natural healing response by providing the highest level of service. Our hope for each patient extends beyond healing; we aspire to help you fulfill your life's mission and purpose abundantly, supporting you in your journey to well-being.</p>
    </section>
    <div class="tile" style="left:819px; top:1165px;">
      <div class="tile-fill navy" role="img" aria-label="Icon of a gear with a wrench"></div>
    </div>

    <footer class="footer">www.<span class="accent">larkmoorchiro</span>.com</footer>
  </main>
</body>
</html>
```